IT Tradingsystem for car dealers needs Business Card Design

We need a fresh and modern design for our new business cards.

We develop a it-business system for car dealers in Sweden, Norway and on our way down to further countries in Europe, hence the namechange to BrolaTek Europe AB. The site can be found at www.brolatek-example.com. The startpage is also in for an update/modernization soon so don't take to much from here.

We are looking to print double sided, 4-colour cards.

We want to look professional, modern and serious. Open to cooler suggestions, but not too crazy. We need to make a good and serious impression on our potential customers. It needs to reflect our scandinavian design values and layout.

Preferably with the full BrolaTek logo in good size on the back, so the small print on the logo can be read easily.

Text that needs to go on the cards:
-------

Per Oskar Fjellström
Founder

Direct +46 70-512 96 47
Support 08-612 57 394
po.fjellstrom@brolatek-example.com

BrolaTek Europe AB
Box 8617
104 29 Stockholm

Brolatek-example.com
Saljportalen-example.se

--------
Good luck and thanks!

PS. If you need more input or see what our previous cards looked like, don't hesitate to contact me!

Target Market(s)

Decision makers / executives at brand cardealers

Industry/Entity Type

Automotive

Contact Information for Business Card

Normal size

Requirements
Must have
• Full logo
Nice to have
• Base on our orange colors
Should not have
• No fonts with serif, and not too much graphics

```html
<!DOCTYPE html>
<html lang="en">
<head>
<meta charset="utf-8">
<title>BrolaTek Business Card</title>
<link rel="stylesheet" href="https://fonts.googleapis.com/css2?family=Roboto:wght@400;500;700;900&display=swap">
<style>
  :root {
    --bg: #dcdcdc;
    --orange: #f37021;
    --orange-light: #f6892a;
    --orange-deep: #ef6a1f;
    --ink: #222222;
    --text: #3a3a3a;
    --white: #ffffff;
  }
  * { box-sizing: border-box; margin: 0; padding: 0; }
  html, body { width: 1200px; height: 900px; overflow: hidden; }
  body {
    background: var(--bg);
    font-family: "Roboto", Arial, sans-serif;
    position: relative;
  }
  .card {
    position: absolute;
    width: 540px;
    height: 336px;
    border-radius: 22px;
    overflow: hidden;
  }
  .card-front { left: 40px; top: 282px; background: var(--white); }
  .card-back {
    left: 620px; top: 282px;
    background: linear-gradient(135deg, var(--orange-light) 0%, var(--orange) 55%, var(--orange-deep) 100%);
  }
  .front-band { position: absolute; left: 0; top: 0; width: 540px; height: 336px; }

  .brand { position: absolute; display: flex; align-items: center; }
  .brand-mark { background: var(--orange); border-radius: 3px; }
  .brand-name { font-weight: 900; letter-spacing: -0.5px; line-height: 1; }
  .brand-tagline { position: absolute; white-space: nowrap; }

  .card-front .brand { left: 120px; top: 38px; }
  .card-front .brand-mark { width: 34px; height: 34px; margin-right: 12px; }
  .card-front .brand-name { font-size: 42px; color: var(--ink); }
  .card-front .brand-tagline { left: 166px; top: 86px; font-size: 10.5px; color: var(--text); }

  .divider { position: absolute; left: 0; top: 150px; width: 540px; height: 2px; background: var(--orange); }

  .person { position: absolute; right: 28px; text-align: right; white-space: nowrap; }
  .person-name { top: 118px; font-size: 22px; font-weight: 700; color: var(--orange); letter-spacing: 0.3px; }
  .person-role { top: 158px; font-size: 12px; font-weight: 500; color: var(--ink); letter-spacing: 0.5px; }

  .contact-list { position: absolute; left: 44px; top: 166px; list-style: none; }
  .contact-list li, .web-list li {
    display: flex; align-items: center; gap: 8px;
    font-size: 12.5px; color: var(--text); height: 20px; white-space: nowrap;
  }
  .icon { width: 13px; height: 13px; flex: none; }

  .web-list { position: absolute; left: 310px; top: 190px; list-style: none; }
  .address { position: absolute; left: 310px; top: 240px; font-size: 12.5px; line-height: 19px; color: var(--text); white-space: nowrap; }

  .card-back .brand { left: 92px; top: 118px; }
  .card-back .brand-mark { width: 44px; height: 44px; margin-right: 16px; background: var(--white); }
  .card-back .brand-name { font-size: 62px; color: var(--white); }
  .card-back .brand-tagline { left: 152px; top: 190px; font-size: 14px; color: var(--white); }
</style>
</head>
<body>

<section class="card card-front" aria-label="Business card front">
  <svg class="front-band" viewBox="0 0 540 336" aria-hidden="true">
    <path d="M0 250 H150 C185 250 205 300 250 336 H0 Z" fill="var(--orange)"/>
    <path d="M0 264 H140 C175 264 190 310 228 336 H0 Z" fill="var(--ink)"/>
  </svg>

  <div class="brand">
    <span class="brand-mark"></span>
    <span class="brand-name">BrolaTek</span>
  </div>
  <p class="brand-tagline">VagnTest | Remarketing | saljportalen-example.se</p>

  <p class="person person-name">PER OSKAR FJELLSTRÖM</p>
  <div class="divider"></div>
  <p class="person person-role">FOUNDER</p>

  <ul class="contact-list">
    <li>
      <svg class="icon" viewBox="0 0 14 14" aria-hidden="true"><rect x="3.5" y="1" width="7" height="12" rx="1.5" fill="none" stroke="var(--orange)" stroke-width="1.3"/></svg>
      +46 70-512 96 47
    </li>
    <li>
      <svg class="icon" viewBox="0 0 14 14" aria-hidden="true"><path d="M3 1.5 L5.2 1.5 L6 4.5 L4.6 5.6 C5.4 7.4 6.6 8.6 8.4 9.4 L9.5 8 L12.5 8.8 L12.5 11 C12.5 12 11.6 12.6 10.6 12.5 C5.8 12 2 8.2 1.5 3.4 C1.4 2.4 2 1.5 3 1.5 Z" fill="var(--orange)"/></svg>
      08-612 57 394
    </li>
    <li>
      <svg class="icon" viewBox="0 0 14 14" aria-hidden="true"><rect x="1" y="3" width="12" height="8.5" fill="none" stroke="var(--orange)" stroke-width="1.3"/><path d="M1 3 L7 8 L13 3" fill="none" stroke="var(--orange)" stroke-width="1.3"/></svg>
      po.fjellstrom@brolatek-example.com
    </li>
  </ul>

  <ul class="web-list">
    <li>
      <svg class="icon" viewBox="0 0 14 14" aria-hidden="true"><circle cx="7" cy="7" r="5.6" fill="none" stroke="var(--orange)" stroke-width="1.2"/><ellipse cx="7" cy="7" rx="2.4" ry="5.6" fill="none" stroke="var(--orange)" stroke-width="1.1"/><path d="M1.4 7 H12.6" stroke="var(--orange)" stroke-width="1.1"/></svg>
      brolatek-example.com
    </li>
    <li>
      <svg class="icon" viewBox="0 0 14 14" aria-hidden="true"><circle cx="8" cy="6" r="4" fill="none" stroke="var(--orange)" stroke-width="1.4"/><path d="M5.2 8.8 L1.5 12.5" stroke="var(--orange)" stroke-width="1.6" stroke-linecap="round"/></svg>
      saljportalen-example.se
    </li>
  </ul>

  <p class="address">BrolaTek Europe AB Box 8617<br>104 29 Stockholm</p>
</section>

<section class="card card-back" aria-label="Business card back">
  <div class="brand">
    <span class="brand-mark"></span>
    <span class="brand-name">BrolaTek</span>
  </div>
  <p class="brand-tagline">VagnTest | Remarketing | saljportalen-example.se</p>
</section>

</body>
</html>
```